Coral Tide Yachting Flyer

Coral Tide Yachting (.com) is a high end luxury and private charter company in the Cayman Islands. All info can be found on our webiste. I currently have a 4 panel roll fold flyer (Can supply working file). I am looking for a new fresh look but also need some changes as we have changes some boats, added some new charter ideas etc.

Between our website and current flyer I think the designer will get the idea. I Welcome new and fresh, I do not need it to match current website, as I may get that changed to.

We are looking for high end and simple/clean and comunicate reliability and professional with a hint of fun in the sun of course. Not whacky and tacky!!

The current PDF's of the current flyer needs a fair bit of changing (For example scuba diving panel will come out and go into a new 1 panel flyer.) I will need 3-4 other flyers too, and a bunch of other stuff in future for new businesses, but starting with this one so I can pick a designer (This is my 1st go with pixel bazaar, always did my own work, but am too busy and am not very good with creativity)

I have logo, support pictures, etc. Have uploaded the basics can email more info and changes after I find a designer. Lots of our boat pictures can be found at http://coraltideyachting-example.com/downloads/maple.zip

Also, we want a panel dedicated to wavorix.com as our big boat now has one onboard and our smaller boat (23') will have two and that will be a dedicated panel (Replace scuba) offering a "Wavorix Extreme Snorkel trip" (I will supply more info on that, once I pick a designer).

Target Market(s)

High end groups. The groups or families that will spend more to get more!!

Industry/Entity Type

It Company

```html
<!DOCTYPE html>
<html lang="en">
<head>
<meta charset="utf-8">
<title>Coral Tide Yachting – Roll Fold Flyer</title>
<link href="https://fonts.googleapis.com/css2?family=Arimo:ital,wght@0,400;0,700;1,700&family=Didact+Gothic&display=swap" rel="stylesheet">
<style>
  :root{
    --bg:#141414;
    --navy:#1b3f8f;
    --teal:#139f9f;
    --aqua:#5fd0d6;
    --red:#e0203a;
    --ink:#24313f;
    --white:#ffffff;
    --sky-top:#2f6fc4;
    --sky-low:#bfe2f5;
    --sea:#1aa6c4;
    --sea-deep:#0d5f95;
  }
  *{box-sizing:border-box;margin:0;padding:0}
  html,body{width:1200px;height:801px;overflow:hidden;background:var(--bg)}
  body{font-family:"Didact Gothic",sans-serif;color:var(--ink)}
  .flyer{position:absolute;left:40px;top:65px;width:1120px;height:671px;display:flex;box-shadow:0 10px 30px rgba(0,0,0,.5)}
  .panel{position:relative;width:280px;height:671px;overflow:hidden}
  .photo{position:absolute}
  .heading{font-family:"Arimo",sans-serif;font-weight:700;font-style:italic}
  .body-copy{position:absolute;font-size:10.5px;line-height:1.35}

  /* Panel 1 */
  .panel-intro{background:linear-gradient(#e6f4fb,#ffffff 40%,#e9f7f8)}
  .panel-intro .yacht-photo{left:0;top:0;width:280px;height:82px;background:linear-gradient(160deg,#7fb6e6,#2b78c2 60%,#1a5c9e)}
  .panel-intro .go-title{position:absolute;left:12px;top:88px;color:var(--navy);font-size:13px}
  .panel-intro .intro-copy{left:12px;top:106px;width:256px}
  .panel-intro .section-title{position:absolute;left:12px;top:160px;color:var(--teal);font-size:21px;line-height:1.05}
  .panel-intro .tagline{position:absolute;left:12px;top:210px;color:var(--red);font-family:"Arimo",sans-serif;font-style:italic;font-weight:700;font-size:13px}
  .panel-intro .palm-photo{left:0;top:232px;width:118px;height:200px;background:linear-gradient(#9cc9ec,#cfe6f3 55%,#e8dcc0)}
  .panel-intro .guests-photo{left:10px;top:440px;width:108px;height:130px;background:linear-gradient(#b8d9ea,#d9c5a8)}
  .panel-intro .charter-copy{left:128px;top:234px;width:142px}
  .panel-intro .cruise-copy{left:128px;top:390px;width:142px}
  .panel-intro .closing{position:absolute;left:128px;top:490px;width:142px;color:var(--teal);font-family:"Arimo",sans-serif;font-weight:700;font-size:14px;line-height:1.2}
  .closing .accent{color:var(--red);display:block;text-align:right;margin-top:6px}

  /* Panel 2 */
  .panel-toy{background:linear-gradient(#ffffff 60%,#dff3f6)}
  .panel-toy .boat-photo{left:0;top:0;width:280px;height:100px;background:linear-gradient(#cfe7f6,#4fa8d8 70%,#2b86c1)}
  .panel-toy .brand{position:absolute;left:14px;top:108px;font-family:"Arimo",sans-serif;font-weight:700;font-size:20px;color:var(--teal);letter-spacing:1px}
  .panel-toy .scooter-photo{left:150px;top:106px;width:118px;height:80px;background:linear-gradient(135deg,#f05a3a,#c91f2a);border-radius:6px}
  .panel-toy .rider-photo{left:14px;top:140px;width:120px;height:46px;background:linear-gradient(#6cc7dc,#2690b8);border-radius:6px}
  .panel-toy .quote{position:absolute;left:0;top:198px;width:280px;text-align:center;font-family:"Arimo",sans-serif;font-weight:700;font-size:19px;line-height:1.15}
  .quote .q-teal{color:var(--teal)}
  .quote .q-red{color:var(--red)}
  .quote .q-light{color:var(--aqua);font-weight:400}
  .quote .q-navy{color:var(--navy);font-size:22px}
  .panel-toy .toy-copy{left:16px;top:300px;width:248px;text-align:center}
  .panel-toy .speedboat-photo{left:20px;top:420px;width:250px;height:130px;background:linear-gradient(#9fd6e6,#3a9cc4 60%,#e9f6fa)}
  .panel-toy .dive-photo{left:0;top:555px;width:170px;height:100px;background:linear-gradient(135deg,#7ec9e0,#f0a03a 70%,#e8c24a)}

  /* Panel 3 */
  .panel-fleet{background:linear-gradient(#2b7fc8,#1b9fc4 50%,#0e6aa0)}
  .panel-fleet .fleet-title{position:absolute;left:12px;color:var(--white);font-size:17px}
  .panel-fleet .voyager-title{top:8px}
  .panel-fleet .voyager-photo{left:0;top:32px;width:280px;height:110px;background:linear-gradient(#cfe8f7,#5cb6e0 55%,#1f7fc0)}
  .panel-fleet .cabin-photo{left:8px;top:150px;width:110px;height:100px;background:linear-gradient(135deg,#d9b88a,#8a6a46);border-radius:4px}
  .panel-fleet .voyager-copy{left:126px;top:152px;width:146px;color:var(--white)}
  .panel-fleet .runner-title{top:300px}
  .panel-fleet .runner-photo{left:0;top:326px;width:280px;height:96px;background:linear-gradient(#e4f3fb,#5ab0dc 60%,#1a5f9a)}
  .panel-fleet .runner-copy{left:12px;top:430px;width:256px;color:var(--white)}
  .panel-fleet .stingray-photo{left:0;top:500px;width:280px;height:171px;background:linear-gradient(#3fc3d6,#1b8fb3)}

  /* Panel 4 – cover */
  .panel-cover{background:var(--white)}
  .panel-cover .sky-photo{left:0;top:0;width:280px;height:320px;background:linear-gradient(var(--sky-top),var(--sky-low) 70%,#e9f6fb)}
  .panel-cover .cover-wave{position:absolute;left:0;top:250px;width:280px;height:120px}
  .panel-cover .mark-dot{position:absolute;left:126px;top:318px;width:28px;height:28px;border-radius:50%;background:var(--teal)}
  .panel-cover .company{position:absolute;left:0;top:354px;width:280px;text-align:center;color:var(--navy);font-size:24px;letter-spacing:1px;line-height:1.1}
  .panel-cover .services{position:absolute;left:0;top:414px;width:280px;text-align:center;color:var(--teal);font-size:12px;letter-spacing:.5px}
  .panel-cover .water-photo{left:0;top:470px;width:280px;height:201px;background:linear-gradient(#8adfe6,var(--sea) 60%,var(--sea-deep))}
  .panel-cover .water-wave{position:absolute;left:0;top:455px;width:280px;height:40px}
</style>
</head>
<body>
<main class="flyer">

  <section class="panel panel-intro">
    <div class="photo yacht-photo" role="img" aria-label="Photo of a white luxury yacht cruising on blue water"></div>
    <h3 class="heading go-title">Go by Yacht!</h3>
    <p class="body-copy intro-copy">For the ultimate in island escapes, step aboard one of our private yachts and let the crew handle every detail while you relax, swim and explore.</p>
    <h2 class="heading section-title">Private Charters<br>&amp; Yachting</h2>
    <p class="tagline">Once in a lifetime...</p>
    <div class="photo palm-photo" role="img" aria-label="Photo of a palm tree on a white sand beach"></div>
    <div class="photo guests-photo" role="img" aria-label="Photo of a family of guests on the beach"></div>
    <p class="body-copy charter-copy">Charter any of our boats including our 60' flagship, for a day that you will never forget. All of our charters can be tailored to your group.</p>
    <p class="body-copy cruise-copy">Cruise around the North Sound, visit secluded beaches and sandbars, or simply unwind on deck.</p>
    <p class="closing">Enjoy the privacy of a chartered vessel for snorkeling, swimming and more... <span class="accent">Priceless!</span></p>
  </section>

  <section class="panel panel-toy">
    <div class="photo boat-photo" role="img" aria-label="Photo of a motor yacht at sea"></div>
    <p class="brand">WAVORIX</p>
    <div class="photo scooter-photo" role="img" aria-label="Photo of red underwater sea scooters"></div>
    <div class="photo rider-photo" role="img" aria-label="Photo of a rider gliding on a sea scooter"></div>
    <p class="quote">
      <span class="q-teal">“The Wavorix is</span><br>
      <span class="q-red">amazingly fast</span><br>
      <span class="q-light">under water,</span><br>
      <span class="q-navy">Like a <span class="q-red">dolphin!</span>”</span>
    </p>
    <p class="body-copy toy-copy">Our customers are looking for the most advanced technical innovation and premium quality. With those priorities in mind we have developed our company philosophy: high performance technology through innovation and quality down to the last detail. Our top of the range class "PREMIER WAVECRAFT" also reflects this approach.</p>
    <div class="photo speedboat-photo" role="img" aria-label="Photo of a white speedboat cutting through waves"></div>
    <div class="photo dive-photo" role="img" aria-label="Photo of a diver riding a yellow sea scooter"></div>
  </section>

  <section class="panel panel-fleet">
    <h3 class="heading fleet-title voyager-title">Lagoon Voyager</h3>
    <div class="photo voyager-photo" role="img" aria-label="Photo of the Lagoon Voyager yacht on turquoise water"></div>
    <div class="photo cabin-photo" role="img" aria-label="Photo of the yacht's interior lounge"></div>
    <p class="body-copy voyager-copy">Our 60' yacht Lagoon Voyager has a cruise speed of 22 knots and all the comforts of home, including 750 sq ft of air-conditioned space and a full kitchen. Up to 12 guests. Call for details.</p>
    <h3 class="heading fleet-title runner-title">Reef Runner</h3>
    <div class="photo runner-photo" role="img" aria-label="Photo of the Reef Runner speedboat"></div>
    <p class="body-copy runner-copy">Our 23' Reef Runner has a top speed of 50 mph and is outstanding for exploring reefs and dive spots. Perfect for groups of up to 8 guests.</p>
    <div class="photo stingray-photo" role="img" aria-label="Photo of a guest meeting a stingray in shallow water"></div>
  </section>

  <section class="panel panel-cover">
    <div class="photo sky-photo" role="img" aria-label="Photo of a girl leaning on a yacht's bow under a blue sky"></div>
    <svg class="cover-wave" viewBox="0 0 280 120" preserveAspectRatio="none" aria-hidden="true">
      <path d="M0 60 C 70 20, 160 10, 280 40 L280 120 L0 120 Z" fill="#ffffff"/>
    </svg>
    <div class="mark-dot" aria-hidden="true"></div>
    <h1 class="company">CORAL TIDE<br>YACHTING</h1>
    <p class="services">Yachting · Diving · Fishing · Snorkeling</p>
    <div class="photo water-photo" role="img" aria-label="Photo of a woman with a stingray in clear turquoise water"></div>
    <svg class="water-wave" viewBox="0 0 280 40" preserveAspectRatio="none" aria-hidden="true">
      <path d="M0 0 L280 0 L280 10 C 200 35, 90 30, 0 14 Z" fill="#ffffff"/>
    </svg>
  </section>

</main>
</body>
</html>
```